A start up Private Wine Label for export to Asia.

We are looking for the best graphic design for our very first wine label Corvessa Vineyards and would like the following requirements:

1. Black background - explore and play around the shade of black
2. Gold Shimmery Colour Font
3. Font should be a cursive classic posh that says Corvessa Vineyards
4. We would like the front graphic design to be simple and elegant and has a traditional classic feel to it.

Target Market(s)

Small scale to test the upper class market for export to Asia

Font styles to use
Script

Colors

Designer to choose colors to be used in the design.

Requirements
Must have
• Gold font for the label Corvessa Vineyards with shimmery touch to it.
• Elegant black background.
• Simple but elegant design.
• Attractive to the upper class market in Asia.
Nice to have
• Explore and play around with your imagination.

```html
<!DOCTYPE html>
<html lang="en">
<head>
<meta charset="utf-8">
<title>Corvessa Vineyards – Cabernet Sauvignon Label</title>
<link rel="stylesheet" href="https://fonts.googleapis.com/css2?family=Mrs+Saint+Delafield&family=Libre+Baskerville:ital,wght@1,700&family=Montserrat:wght@700&display=swap">
<style>
  :root {
    --page-black: #030303;
    --label-black: #0a0a0a;
    --engraving-dark: #141414;
    --engraving-light: #2a2a2a;
    --gold-light: #f3dc9a;
    --gold-mid: #d4b266;
    --gold-deep: #a8843f;
  }
  html, body {
    margin: 0;
    padding: 0;
    width: 1200px;
    height: 1200px;
    overflow: hidden;
    background: var(--page-black);
  }
  .canvas {
    position: relative;
    width: 1200px;
    height: 1200px;
  }
  .wine-label {
    position: absolute;
    left: 100px;
    top: 190px;
    width: 1000px;
    height: 820px;
    background: var(--label-black);
    overflow: hidden;
  }
  .dragon-engraving {
    position: absolute;
    inset: 0;
    background:
      radial-gradient(ellipse 28% 50% at 22% 55%, var(--engraving-light), transparent 70%),
      radial-gradient(ellipse 28% 50% at 78% 55%, var(--engraving-light), transparent 70%),
      linear-gradient(90deg, var(--engraving-dark), var(--label-black) 50%, var(--engraving-dark));
  }
  .brand-name {
    position: absolute;
    top: 115px;
    left: 0;
    right: 0;
    margin: 0;
    text-align: center;
    font-family: "Mrs Saint Delafield", cursive;
    font-weight: 400;
    font-size: 116px;
    line-height: 1;
    color: var(--gold-mid);
  }
  .varietal {
    position: absolute;
    top: 668px;
    left: 0;
    right: 0;
    margin: 0;
    text-align: center;
    font-family: "Libre Baskerville", serif;
    font-style: italic;
    font-weight: 700;
    font-size: 40px;
    line-height: 1;
    color: var(--gold-mid);
  }
  .region {
    position: absolute;
    top: 722px;
    left: 0;
    right: 0;
    margin: 0;
    text-align: center;
    font-family: "Montserrat", sans-serif;
    font-weight: 700;
    font-size: 44px;
    letter-spacing: 5px;
    line-height: 1;
    background: linear-gradient(180deg, var(--gold-light), var(--gold-mid) 55%, var(--gold-deep));
    -webkit-background-clip: text;
    background-clip: text;
    color: transparent;
  }
</style>
</head>
<body>
  <main class="canvas">
    <section class="wine-label">
      <div class="dragon-engraving" role="img" aria-label="Two mirrored engraved dragons facing each other, tone-on-tone black"></div>
      <h1 class="brand-name">Corvessa Vineyards</h1>
      <p class="varietal">Cabernet Sauvignon</p>
      <p class="region">BAROSSA VALLEY</p>
    </section>
  </main>
</body>
</html>
```